IT Company Business Card Rebranding

We want to modernize our business cards massively. We want to incorporate aspects of our old business card such as the white and geometric design with the blues of another icon. Existing Logo, old business card and icon are all attached.

We are a modern IT company that provides support for new and growing technologies and want our business cards to be modern yet professional.
Updates

Note: Do not use file ICON.png in design. This is just a design we like Added Wednesday, March 9, 2016

Industry/Entity Type

Information Technology

Contact Information for Business Card

Roughly 43 : 26 or 1075 x 650 px

Font styles to use
Serif

Colors
0492cd
3276b5
33a6d7
86cfc6
cfeae6
cee9f5
ffffff

Requirements
Must have
• Modern yet professional
Nice to have
• We would like to incorporate the blues of our existing logo and of the icon provided. Really like the design of the icon.
Should not have
• Too Decorative. Just simple and professional.
• Not have the circle icon, as it is a copyrighted icon, I just like the colors and the geometric design

```html
<!DOCTYPE html>
<html lang="en">
<head>
<meta charset="utf-8">
<title>Nexora Tech – Business Card</title>
<link rel="stylesheet" href="https://fonts.googleapis.com/css2?family=Source+Serif+4:opsz,wght@8..60,300;8..60,400;8..60,700&display=swap">
<style>
  :root {
    --canvas: #e9ebed;
    --card: #ffffff;
    --blue-main: #0f7bc4;
    --blue-deep: #3276b5;
    --blue-sky: #33a6d7;
    --teal: #1ea3b5;
    --mint: #86cfc6;
    --mint-pale: #cfeae6;
    --sky-pale: #cee9f5;
    --wordmark: #8a8d92;
    --facet-light: #f4f4f5;
    --facet-dark: #d9dadc;
    --text-light: #ffffff;
  }
  * { box-sizing: border-box; margin: 0; padding: 0; }
  html, body {
    width: 1200px; height: 900px; overflow: hidden;
    background: var(--canvas);
    font-family: "Source Serif 4", Georgia, serif;
  }
  .canvas { position: relative; width: 1200px; height: 900px; }
  .card {
    position: absolute; left: 280px;
    width: 640px; height: 387px;
    background: var(--card);
    box-shadow: 0 6px 18px rgba(0,0,0,0.12);
    overflow: hidden;
  }
  .card--front { top: 42px; }
  .card--back { top: 471px; }

  /* Front */
  .brand {
    position: absolute; left: 0; right: 0; top: 130px;
    display: flex; align-items: center; justify-content: center; gap: 18px;
  }
  .brand__dot {
    width: 24px; height: 24px; border-radius: 50%;
    background: var(--blue-deep);
  }
  .brand__name {
    font-weight: 300; font-size: 34px; letter-spacing: 11px;
    color: var(--wordmark); text-transform: uppercase;
  }
  .facet-band {
    position: absolute; left: 0; right: 0; bottom: 0; height: 120px;
    background: linear-gradient(180deg, rgba(244,244,245,0) 0%, var(--facet-light) 35%, var(--facet-dark) 100%);
  }

  /* Back */
  .back-shapes { position: absolute; inset: 0; }
  .artwork {
    position: absolute; left: 70px; top: 78px;
    width: 210px; height: 230px;
    background: linear-gradient(160deg, var(--mint-pale) 0%, var(--sky-pale) 100%);
  }
  .contact {
    position: absolute; right: 42px; top: 166px;
    text-align: right; color: var(--text-light);
  }
  .contact__name { font-weight: 700; font-size: 21px; line-height: 1.1; letter-spacing: 0.5px; }
  .contact__role { font-weight: 400; font-size: 16px; line-height: 1.25; margin-bottom: 16px; }
  .contact__line {
    display: flex; justify-content: flex-end; align-items: center; gap: 12px;
    font-size: 16px; line-height: 1.4;
  }
  .contact__icon { width: 13px; height: 13px; flex: none; }
</style>
</head>
<body>
<main class="canvas">

  <section class="card card--front" aria-label="Card front">
    <div class="brand">
      <span class="brand__dot"></span>
      <span class="brand__name">Nexora Tech</span>
    </div>
    <div class="facet-band" role="img" aria-label="Soft grey low-poly geometric relief along the lower edge"></div>
  </section>

  <section class="card card--back" aria-label="Card back">
    <svg class="back-shapes" width="640" height="387" viewBox="0 0 640 387">
      <path d="M282,0 C372,90 362,270 205,387 L640,387 L640,0 Z" fill="var(--teal)"/>
      <path d="M300,0 C388,95 378,275 226,387 L640,387 L640,0 Z" fill="#ffffff"/>
      <path d="M306,0 C394,97 384,277 234,387 L640,387 L640,0 Z" fill="var(--blue-main)"/>
    </svg>

    <div class="artwork" role="img" aria-label="Area for geometric faceted artwork in pale teal and blue tones"></div>

    <div class="contact">
      <p class="contact__name">MILO</p>
      <p class="contact__role">technical services</p>
      <p class="contact__line">055-987 654 321
        <svg class="contact__icon" viewBox="0 0 16 16"><path d="M4 1 L6.5 4.5 L5 6.5 C6 8.5 7.5 10 9.5 11 L11.5 9.5 L15 12 L13 15 C7 14.5 1.5 9 1 3 Z" fill="#fff"/></svg>
      </p>
      <p class="contact__line">info@nexoratech.com
        <svg class="contact__icon" viewBox="0 0 16 16"><rect x="1" y="3" width="14" height="10" fill="#fff"/><path d="M1 3 L8 9 L15 3" fill="none" stroke="#0f7bc4" stroke-width="1.4"/></svg>
      </p>
      <p class="contact__line">www.nexoratech.com
        <svg class="contact__icon" viewBox="0 0 16 16"><circle cx="8" cy="8" r="7" fill="#fff"/><path d="M1 8 H15 M8 1 C4 5 4 11 8 15 M8 1 C12 5 12 11 8 15" fill="none" stroke="#0f7bc4" stroke-width="1.1"/></svg>
      </p>
    </div>
  </section>

</main>
</body>
</html>
```